Charity fundraising company - need eDM design!

We are a telemarketing company working with charities to raise money from individuals via regular monthly direct debits or credit card payments. The audience for this eDM is a few hundred fundraising managers. We want to provide a clearly laid-out email to deliver our offer of a free telemarketing consultation.

The eDM will be sent via Mailchimp.

Industry/Entity Type

Charity

Logo Text

KELP Dial

Font styles to use
Sans Serif
Other font styles liked:
• Helvetica Neue

Requirements
Nice to have
• Our values:
• Storytelling with passion
• Fundraising with integrity
• Results that deliver a strong return on your charity's investment.
Should not have
• Logo at the top of the eDM (please place at the bottom)

```html
<!DOCTYPE html>
<html lang="en">
<head>
<meta charset="utf-8">
<title>KELP Dial – Free Telemarketing Consultation eDM</title>
<link rel="stylesheet" href="https://fonts.googleapis.com/css2?family=Open+Sans:wght@400;600;700&display=swap">
<style>
  :root {
    --stage: #d6d6d6;
    --paper: #ffffff;
    --header-grey: #ececec;
    --text-grey: #707070;
    --body-grey: #6f6f6f;
    --brand-blue: #1eaeea;
    --rule: #e2e2e2;
    --footer-dark: #3f3d4a;
    --white: #ffffff;
    --logo-ink: #3a3a3a;
    --photo-agent-a: #2b2a2c;
    --photo-agent-b: #6a5548;
    --photo-headset-a: #f2f2f2;
    --photo-headset-b: #9a9a9a;
  }
  * { box-sizing: border-box; margin: 0; padding: 0; }
  html, body {
    width: 960px; height: 1200px; overflow: hidden;
    background: var(--stage);
    font-family: "Open Sans", "Helvetica Neue", Arial, sans-serif;
  }
  .edm {
    position: absolute; left: 120px; top: 189px;
    width: 720px; background: var(--paper);
  }
  .edm-headline {
    height: 55px; background: var(--header-grey);
    display: flex; align-items: center; justify-content: center;
    color: var(--text-grey); font-size: 24px; font-weight: 400;
  }
  .row { display: flex; }
  .intro { height: 221px; }
  .intro-panel {
    width: 360px; background: var(--brand-blue); color: var(--white);
    display: flex; align-items: center; justify-content: center;
    padding: 0 40px; text-align: center;
    font-size: 20px; font-weight: 700; line-height: 1.27;
  }
  .photo-agent {
    flex: 1;
    background: radial-gradient(circle at 62% 45%, var(--photo-agent-b) 0%, var(--photo-agent-a) 62%);
  }
  .offer { height: 268px; }
  .photo-headset {
    width: 359px;
    background: radial-gradient(circle at 40% 50%, var(--photo-headset-a) 0%, #cfcfcf 55%, var(--photo-headset-b) 100%);
  }
  .offer-list { flex: 1; padding: 14px 6px 0 17px; }
  .offer-title {
    color: var(--text-grey); font-size: 20px; font-weight: 600;
    text-align: center; margin-bottom: 16px;
  }
  .offer-item {
    display: flex; gap: 14px; list-style: none;
    color: var(--body-grey); font-size: 15.4px; line-height: 1.35;
    margin-bottom: 11px;
  }
  .offer-item svg { flex: none; margin-top: 2px; }
  .cta-area {
    height: 150px; border-top: 1px solid var(--rule); border-bottom: 1px solid var(--rule);
    display: flex; align-items: center; justify-content: center;
  }
  .cta-button {
    width: 382px; height: 91px; border-radius: 46px;
    background: var(--brand-blue); color: var(--white);
    display: flex; flex-direction: column; align-items: center; justify-content: center;
    font-weight: 700; font-size: 16.8px; line-height: 1.65; text-decoration: none;
  }
  .cta-title { letter-spacing: 0.3px; }
  .contact-bar {
    height: 86px; display: flex; align-items: center;
    padding: 0 0 0 12px; font-size: 11.5px; color: var(--body-grey); font-weight: 600;
  }
  .brand-mark {
    width: 200px; display: flex; align-items: center; gap: 8px;
    color: var(--logo-ink); font-size: 24px; font-weight: 700;
  }
  .brand-mark .square { width: 16px; height: 16px; background: var(--logo-ink); }
  .contact-address { width: 286px; display: flex; gap: 8px; line-height: 1.4; padding-left: 20px; }
  .contact-lines { display: flex; flex-direction: column; gap: 9px; }
  .contact-line { display: flex; align-items: center; gap: 16px; }
  .legal-bar {
    height: 42px; background: var(--footer-dark); color: var(--white);
    display: flex; align-items: center; justify-content: space-between;
    padding: 0 38px 0 35px; font-size: 16px;
  }
</style>
</head>
<body>
  <main class="edm">
    <header class="edm-headline">Want more regular givers for your cause?</header>

    <section class="row intro">
      <div class="intro-panel">KELP Dial is Australia’s leading telemarketing specialist for acquiring new regular givers through lead generation.</div>
      <div class="photo-agent" role="img" aria-label="Smiling call-centre agent wearing a headset, working at a computer"></div>
    </section>

    <section class="row offer">
      <div class="photo-headset" role="img" aria-label="Black telephone headset resting on a pale grey surface"></div>
      <div class="offer-list">
        <h2 class="offer-title">Speak to us today and we will:</h2>
        <ul>
          <li class="offer-item">
            <svg width="19" height="19" viewBox="0 0 20 20" aria-hidden="true"><circle cx="10" cy="10" r="8" fill="none" stroke="#777" stroke-width="2.4"/><path d="M6 10 l3 3 l8-8" fill="none" stroke="#777" stroke-width="2.6" stroke-linecap="round"/></svg>
            <span>Run a no-obligation TM donor acquisition feasibility assessment for you.</span>
          </li>
          <li class="offer-item">
            <svg width="19" height="19" viewBox="0 0 20 20" aria-hidden="true"><circle cx="10" cy="10" r="8" fill="none" stroke="#777" stroke-width="2.4"/><path d="M6 10 l3 3 l8-8" fill="none" stroke="#777" stroke-width="2.6" stroke-linecap="round"/></svg>
            <span>Offer a Cost Per Acquisition model, with a sliding scale of fees based on the volume of leads provided.</span>
          </li>
          <li class="offer-item">
            <svg width="19" height="19" viewBox="0 0 20 20" aria-hidden="true"><circle cx="10" cy="10" r="8" fill="none" stroke="#777" stroke-width="2.4"/><path d="M6 10 l3 3 l8-8" fill="none" stroke="#777" stroke-width="2.6" stroke-linecap="round"/></svg>
            <span>Handle the entire data ordering and management process for you at no additional cost.</span>
          </li>
        </ul>
      </div>
    </section>

    <section class="cta-area">
      <a class="cta-button" href="#">
        <span class="cta-title">FREE NO-OBLIGATION CONSULTATION</span>
        <span class="cta-sub">Drop us a line today...</span>
      </a>
    </section>

    <footer>
      <div class="contact-bar">
        <div class="brand-mark"><span class="square"></span>KELP Dial</div>
        <div class="contact-address">
          <svg width="18" height="18" viewBox="0 0 20 20" aria-hidden="true"><circle cx="10" cy="10" r="8.5" fill="none" stroke="#1eaeea" stroke-width="1.6"/><path d="M10 5.5 a3 3 0 0 1 3 3 c0 2.3-3 5.5-3 5.5 s-3-3.2-3-5.5 a3 3 0 0 1 3-3z" fill="none" stroke="#1eaeea" stroke-width="1.4"/></svg>
          <span>Suite 3.14, Level 3, 27 Harbour Lane,<br>Sydney, NSW, 2000</span>
        </div>
        <div class="contact-lines">
          <div class="contact-line">
            <svg width="18" height="18" viewBox="0 0 20 20" aria-hidden="true"><circle cx="10" cy="10" r="8.5" fill="none" stroke="#1eaeea" stroke-width="1.6"/><path d="M7 6 l2 2 l-1 1.3 c.7 1.3 1.5 2.1 2.7 2.7 l1.3-1 l2 2 l-1.3 1.3 c-3.2-.4-6.3-3.5-6.7-6.7z" fill="#1eaeea"/></svg>
            <span>02 9100 5500</span>
          </div>
          <div class="contact-line">
            <svg width="18" height="18" viewBox="0 0 20 20" aria-hidden="true"><circle cx="10" cy="10" r="8.5" fill="none" stroke="#1eaeea" stroke-width="1.6"/><path d="M8.6 11.4 l2.8-2.8 M9.2 7.6 l1.2-1.2 a2 2 0 0 1 2.8 2.8 l-1.2 1.2 M10.8 12.4 l-1.2 1.2 a2 2 0 0 1-2.8-2.8 l1.2-1.2" fill="none" stroke="#1eaeea" stroke-width="1.4" stroke-linecap="round"/></svg>
            <span>www.kelpdial.com</span>
          </div>
        </div>
      </div>
      <div class="legal-bar">
        <span>KELP Dial 2016 All rights reserved.</span>
        <span>Unsubscribe here</span>
      </div>
    </footer>
  </main>
</body>
</html>
```